Hearth & Keg Room requires web site design - Casual restaurant

Need website designed for re-branding of Restaurant based in Fort Morgan, Colorado. We offer a wide variety of American cuisine in a casual, rustic atmosphere. We're offering 16 craft beers on draft, as well as a full service bar, and modern, interesting menu selections in a friendly, fun and energetic environment, with an emphasis on superior customer service and high quality, locally sourced food. We are a family, and community service oriented establishment. The website design should convey a welcoming sense, "simplicity", yet sophisticated - without pretentiousness. The website should effectively convey our "home style" relaxed atmosphere, as well as our casual character.

Business Hours: Sunday - Thursday, 11am-10pm / Friday & Saturday, 11am-11am

The Dunlo Hearth & Keg Room
2736 Pennick Road
Fort Morgan, Colorado 80701
B: (970) 555-0173

WEBSITE ADDRESS: thedunlokegroom.com

Target Market(s)

Young Adults
Families
Blue and White Collar Americans
Senior Citizens
Small town location, appeal to everyone

Industry/Entity Type

American Restaurant

Contact Information for Business Card

Marcus T Ellery
Food & Beverage Director
2736 Pennick Road
B: (970) 555-0173
M: (231) 555-0148
mtellery@dunlokegroom.com
www.thedunlokegroom.com
***Use logo in uploaded files
***Open to single OR double sided
*** I will have additional names and information to add to this, for other employees.

Coding

Coded - Design and coding required

Number of Pages Required

5+ page

Font styles to use
Serif
Sans Serif
Decorative
Other font styles liked:
• Calafornian FB,

Requirements
Must have
• Home/Welcome Page
• Menu Page/Online Ordering Ready
• About Us/Contact Us page
• Catering/Private Events/Banquets Advertising section
• Ability to link to Pagebook/TripNotes/Yapper/Instagram etc.
• Logo uploaded, reference for colors as well.
Nice to have
• About craft beer page
• Our Story/Bio section
• Photo Gallery
• Employment/Apply section
Should not have
• We are NOT a "fine dining" restaurant... think casual...

```html
<!DOCTYPE html>
<html lang="en">
<head>
<meta charset="utf-8">
<title>The Dunlo Hearth &amp; Keg Room</title>
<link href="https://fonts.googleapis.com/css2?family=Fira+Mono&family=Fira+Sans:wght@500;600&family=Lato:wght@400;700&display=swap" rel="stylesheet">
<style>
  :root {
    --paper: #ffffff;
    --ink: #111111;
    --nav-ink: #2a2a2a;
    --muted: #c9c9c9;
    --rule: #e6e6e6;
    --nav-rule: #8a8a8a;
    --goose-dark: #2b2b2b;
    --goose-mid: #6d6d6d;
    --goose-light: #bdbdbd;
  }
  * { margin: 0; padding: 0; box-sizing: border-box; }
  html, body { width: 1200px; height: 518px; overflow: hidden; background: var(--paper); }
  .hero { position: relative; width: 1200px; height: 518px; }

  .social { position: absolute; left: 76px; top: 44px; list-style: none; font-family: "Lato", sans-serif; font-weight: 700; font-size: 14px; }
  .social li { margin-bottom: 8px; }
  .social a { color: var(--muted); text-decoration: none; display: inline-block; padding-bottom: 4px; border-bottom: 1px solid var(--rule); }

  .contact { position: absolute; right: 72px; top: 43px; text-align: right; font-family: "Lato", sans-serif; font-weight: 700; font-size: 12.5px; line-height: 20px; color: var(--muted); }
  .contact a { color: var(--muted); text-decoration: none; border-bottom: 1px dotted var(--muted); }

  .goose-art { position: absolute; left: 624px; top: 90px; width: 306px; height: 300px;
    border-radius: 46% 40% 30% 30%;
    background: radial-gradient(ellipse at 62% 60%, var(--goose-dark) 0%, var(--goose-mid) 45%, var(--goose-light) 72%, rgba(255,255,255,0) 90%); }

  .review { position: absolute; left: 160px; top: 152px; }
  .review-quote { font-family: "Fira Sans", sans-serif; font-weight: 600; font-size: 31px; letter-spacing: 1.5px; color: var(--ink); line-height: 1.2; }
  .review-source { margin-top: 5px; font-family: "Fira Mono", monospace; font-size: 18px; color: var(--ink); letter-spacing: 0.5px; }

  .brand { position: absolute; left: 70px; top: 420px; font-family: "Fira Sans", sans-serif; font-weight: 600; color: var(--ink); }
  .brand-name { font-size: 30px; line-height: 1; letter-spacing: -0.5px; }
  .brand-sub { font-size: 11px; letter-spacing: 0.4px; margin-top: 4px; }

  .main-nav { position: absolute; right: 76px; top: 452px; display: flex; gap: 38px; list-style: none; font-family: "Lato", sans-serif; font-size: 13px; letter-spacing: 3px; }
  .main-nav a { color: var(--nav-ink); text-decoration: none; display: inline-block; padding-bottom: 6px; border-bottom: 1px solid var(--nav-rule); margin-right: -3px; }
</style>
</head>
<body>
<main class="hero">
  <ul class="social">
    <li><a href="#">Pagebook</a></li>
    <li><a href="#">TripNotes</a></li>
    <li><a href="#">Yapper</a></li>
  </ul>

  <div class="contact">
    <a href="#">hello@dunlokegroom.com</a><br>
    (970) 555-0173
  </div>

  <div class="goose-art" role="img" aria-label="Engraved black and white illustration of a standing goose"></div>

  <blockquote class="review">
    <p class="review-quote">Flowless. Best goose you will ever taste.</p>
    <p class="review-source">- Elena Varga, The Plains Ledger</p>
  </blockquote>

  <div class="brand">
    <div class="brand-name">The Dunlo</div>
    <div class="brand-sub">Hearth &amp; Keg Room</div>
  </div>

  <ul class="main-nav">
    <li><a href="#">ABOUT</a></li>
    <li><a href="#">MENU</a></li>
    <li><a href="#">RESERVATION</a></li>
    <li><a href="#">BLOG</a></li>
    <li><a href="#">CONTACT</a></li>
    <li><a href="#">DEMOS</a></li>
  </ul>
</main>
</body>
</html>
```